Create Lanternfield HR Business Cards.

Create Business Cards for Lanternfield HR. 2 sided and Would like the back to have the logo.

Info for Business Card:
Address: 4827 Millbrook Ave Suite 230 Cleveland, Ohio 44987
Office Number: 216-555-0143
Mobile: 216-555-0192

Website: www.lanternfieldhr.example

Target Market(s)

Small to medium size businesses

Industry/Entity Type

Human Resources

Contact Information for Business Card

Company logo and information

Font styles to use
Serif
Sans Serif

Requirements
Must have
• Info for Business Card: Address: 4827 Millbrook Ave Suite 230 Cleveland, Ohio 44987 Office Number: 216-555-0143 Mobile: 216-555-0192 Website: www.lanternfieldhr.example

```html
<!DOCTYPE html>
<html lang="en">
<head>
<meta charset="utf-8">
<title>Lanternfield HR Business Cards</title>
<link rel="stylesheet" href="https://fonts.googleapis.com/css2?family=Montserrat:wght@700;800&family=Open+Sans:wght@400;600&display=swap">
<style>
  :root {
    --stage: #222222;
    --navy: #29255f;
    --orange: #f58a21;
    --white: #ffffff;
    --ink: #141414;
  }
  * { box-sizing: border-box; margin: 0; padding: 0; }
  html, body { width: 1200px; height: 711px; overflow: hidden; background: var(--stage); }
  .stage { position: relative; width: 1200px; height: 711px; }
  .card {
    position: absolute; top: 207px; width: 520px; height: 297px;
    border-radius: 20px; overflow: hidden;
  }
  .card--back { left: 50px; background: var(--navy); }
  .card--front { left: 630px; background: var(--white); }

  .brand {
    position: absolute; display: flex; align-items: center; gap: 12px;
    font-family: "Montserrat", sans-serif; font-weight: 800; white-space: nowrap;
  }
  .brand__dot { border-radius: 50%; flex: none; }
  .card--back .brand {
    left: 0; right: 0; top: 0; bottom: 0; justify-content: center;
    color: var(--white); font-size: 40px;
  }
  .card--back .brand__dot { width: 34px; height: 34px; background: var(--white); }
  .card--front .brand {
    left: 26px; top: 106px; color: var(--navy); font-size: 19px; gap: 8px;
  }
  .card--front .brand__dot { width: 16px; height: 16px; background: var(--orange); }

  .divider {
    position: absolute; left: 238px; top: 36px; width: 1px; height: 150px;
    background: var(--orange);
  }
  .details { position: absolute; left: 256px; top: 28px; color: var(--ink); font-family: "Open Sans", sans-serif; }
  .details__name {
    font-family: "Montserrat", sans-serif; font-weight: 800; font-size: 28px; line-height: 1;
  }
  .details__name .first { color: var(--orange); }
  .details__name .last { color: var(--navy); }
  .details__role {
    font-family: "Montserrat", sans-serif; font-weight: 700; font-size: 12px; margin-top: 3px;
  }
  .details__address { font-size: 11px; line-height: 1.35; margin-top: 10px; }
  .contact { list-style: none; margin-top: 8px; font-size: 11px; line-height: 1.4; }
  .contact li { display: flex; align-items: center; gap: 7px; }
  .contact svg { width: 12px; height: 12px; flex: none; }
  .wave { position: absolute; left: 0; bottom: 0; width: 520px; height: 297px; }
</style>
</head>
<body>
<main class="stage">
  <section class="card card--back" aria-label="Card back">
    <div class="brand"><span class="brand__dot"></span>Lanternfield HR</div>
  </section>

  <section class="card card--front" aria-label="Card front">
    <svg class="wave" viewBox="0 0 520 297" aria-hidden="true">
      <path fill="var(--navy)" d="M0 252 C180 258 310 238 400 208 C455 190 490 182 520 180 L520 194 C490 196 458 204 405 222 C315 252 180 272 0 266 Z"/>
      <path fill="var(--orange)" d="M0 274 C185 276 320 256 410 228 C462 211 492 202 520 200 L520 297 L0 297 Z"/>
    </svg>

    <div class="brand"><span class="brand__dot"></span>Lanternfield HR</div>
    <div class="divider"></div>

    <div class="details">
      <h1 class="details__name"><span class="first">Your</span> <span class="last">Name</span></h1>
      <p class="details__role">Managing Director</p>
      <p class="details__address">4827 Millbrook Ave Suite 230<br>Cleveland, Ohio 44987</p>
      <ul class="contact">
        <li><svg viewBox="0 0 12 12"><path fill="var(--navy)" d="M2.5 1 L4.5 1 L5.2 3.6 L4 4.5 C4.6 5.9 6 7.3 7.5 8 L8.4 6.8 L11 7.5 L11 9.5 C11 10.3 10.3 11 9.5 11 C5 11 1 7 1 2.5 C1 1.7 1.7 1 2.5 1 Z"/></svg>216-555-0143</li>
        <li><svg viewBox="0 0 12 12"><rect x="2.5" y="0.8" width="7" height="10.4" rx="1.2" fill="none" stroke="var(--orange)" stroke-width="1.2"/><circle cx="6" cy="9" r="0.8" fill="var(--orange)"/></svg>216-555-0192</li>
        <li><svg viewBox="0 0 12 12"><circle cx="6" cy="6" r="5" fill="var(--navy)"/><path d="M1 6 H11 M6 1 C3.5 3.5 3.5 8.5 6 11 M6 1 C8.5 3.5 8.5 8.5 6 11" fill="none" stroke="var(--white)" stroke-width="0.7"/></svg>www.lanternfieldhr.example</li>
        <li><svg viewBox="0 0 12 12"><rect x="0.8" y="2.5" width="10.4" height="7.5" rx="0.8" fill="var(--orange)"/><path d="M1 3 L6 7 L11 3" fill="none" stroke="var(--white)" stroke-width="0.9"/></svg>info@LanternfieldHR.example</li>
      </ul>
    </div>
  </section>
</main>
</body>
</html>
```